Retail packaging for chocolate souvenir

We require graphic design for an Australian-made chocolate boomerang. We need an A4 size page which contains 4 boomerangs. The length of the boomerangs will all be the same size (180mm length). This can be provided. If 4 boomerangs, we want two different designs (2 x one design) + (2 x another design). Looking for simple Australian aboriginal artwork, but something original not a cut n paste job of existing boomerangs. I have attached an example of some boomerang art that is simple. I would like a kangaroo (in aboriginal artwork) in the middle and balanced by the same aboriginal art either side. Also looking for another animal (koala) and balanced by the same aboriginal artwork either side.
In addition to the A4 page with 4 boomerangs, we need a design for the small retail box that will contain it. We need two retail boxes - one for milk chocolate boomerang and one for dark chocolate boomerang. They need to look the same and even have the same graphics, but need to be different colouring to differentiate between milk chocolate and dark chocolate. The dimensions of the retail box will be 210mm long x 20mm deep x 120mm high. We need an open window to show case the boomerang with a 15mm wide frame on the sides and bottom, and a 25mm wide above the boomerang window. I have attached a first draft example. Please note the attached file template is not accurate and does not even form a 3D box.
Target Market(s)
Tourists visiting Australia
Requirements
Must have
- Graphics must be in Australian aboriginal artwork. Must look impressive, appealing for tourists. This product is aimed at tourists visiting Australia, so needs to show case Australia. The graphics for the A4 transfer sheet need to be earthy, Australian aboriginal colours (white, red, orange, yellow, etc). Please keep in mind these colours will be imprinted onto milk chocolate (brown) and dark chocolate (dark brown). Therefore, dark colours WILL NOT show up. Also, the images for the A4 transfer sheet needs to be MIRROR IMAGE so when they are applied to the chocolate it will be read/seen correctly.
Nice to have
- The retail box will be cardboard but I would love to see some shiny metallic colours on the retail box to draw attention to the customer. Not sure if this is possible.

```html
<!DOCTYPE html>
<html lang="en">
<head>
<meta charset="utf-8">
<title>Outback Treats – Chocolate Boomerang Retail Boxes</title>
<link href="https://fonts.googleapis.com/css2?family=Ultra&family=Montserrat:wght@400;500&display=swap" rel="stylesheet">
<style>
  :root {
    --canvas-bg: #ecebea;
    --dark-top: #5a2a2c;
    --dark-mid: #2e1214;
    --dark-bottom: #1a0809;
    --silver-light: #f4f4f4;
    --silver-mid: #c9c9c9;
    --silver-dark: #9a9a9a;
    --label-dark: #2a2222;
    --ink-white: #ffffff;
    --ink-dark: #2a2222;
    --art-red: #c8321c;
    --art-orange: #ef8a2a;
    --art-cream: #f6d6a8;
    --art-pink: #e4505a;
    --art-brown: #3a1214;
  }
  * { box-sizing: border-box; margin: 0; padding: 0; }
  html, body { width: 1200px; height: 1200px; overflow: hidden; background: var(--canvas-bg); }
  .canvas {
    position: relative; width: 1200px; height: 1200px;
    display: flex; justify-content: center; align-items: center; gap: 80px;
  }
  .box-front {
    position: relative; width: 480px; height: 820px; overflow: hidden;
    box-shadow: 0 18px 40px rgba(0,0,0,.25);
  }
  .box-front--dark { background: linear-gradient(180deg, var(--dark-top) 0%, var(--dark-mid) 45%, var(--dark-bottom) 100%); }
  .box-front--milk { background: linear-gradient(160deg, var(--silver-light) 0%, var(--silver-mid) 55%, var(--silver-light) 100%); }
  .hang-tab {
    position: absolute; top: 0; left: 50%; width: 150px; height: 26px; transform: translateX(-50%);
    border-radius: 0 0 6px 6px;
  }
  .box-front--dark .hang-tab { background: linear-gradient(90deg, var(--silver-dark), var(--silver-light), var(--silver-dark)); }
  .box-front--milk .hang-tab { background: var(--label-dark); }
  .brand-label {
    position: absolute; top: 110px; left: 0; width: 370px; height: 160px;
    display: flex; align-items: center; justify-content: center; gap: 16px;
  }
  .box-front--dark .brand-label { background: linear-gradient(120deg, var(--silver-dark), var(--silver-light) 50%, var(--silver-mid)); }
  .box-front--milk .brand-label { background: var(--label-dark); }
  .brand-mark { width: 22px; height: 22px; }
  .brand-name { font-family: "Ultra", serif; font-size: 38px; line-height: 1; }
  .box-front--dark .brand-mark { background: var(--ink-dark); }
  .box-front--dark .brand-name { color: var(--ink-dark); }
  .box-front--milk .brand-mark { background: var(--silver-light); }
  .box-front--milk .brand-name { color: var(--silver-light); }
  .range-line {
    position: absolute; top: 292px; left: 40px;
    font-family: "Montserrat", sans-serif; font-size: 17px; letter-spacing: 2px;
  }
  .box-front--dark .range-line { color: #bfb3b3; }
  .box-front--milk .range-line { color: #555; }
  .flavour {
    position: absolute; top: 370px; left: 0; width: 300px; text-align: center;
    font-family: "Ultra", serif; font-size: 36px; line-height: 1.15;
  }
  .box-front--dark .flavour { color: var(--ink-white); }
  .box-front--milk .flavour { color: var(--ink-dark); }
  .artwork { position: absolute; left: 0; bottom: 0; width: 480px; height: 420px; }
  .weight-badge {
    position: absolute; left: 30px; bottom: 150px; width: 70px; height: 70px; border-radius: 50%;
    background: var(--ink-white); display: flex; align-items: center; justify-content: center;
    font-family: "Ultra", serif; font-size: 22px; color: var(--ink-dark);
  }
</style>
</head>
<body>
<main class="canvas">

  <section class="box-front box-front--dark">
    <div class="hang-tab"></div>
    <div class="brand-label"><span class="brand-mark"></span><span class="brand-name">Outback Treats</span></div>
    <p class="range-line">CHOCOLATE BOOMERANGS</p>
    <h2 class="flavour">Dark<br>Chocolate<br>Boomerang</h2>
    <svg class="artwork" viewBox="0 0 480 420" role="img" aria-label="Aboriginal dot-painting artwork of kangaroos in red, orange, cream and white">
      <defs>
        <linearGradient id="artDark" x1="0" y1="1" x2="1" y2="0">
          <stop offset="0" stop-color="#e4505a"/>
          <stop offset=".45" stop-color="#ef8a2a"/>
          <stop offset="1" stop-color="#c8321c"/>
        </linearGradient>
      </defs>
      <path d="M0 420 L0 360 C60 320 140 300 220 280 C280 260 320 200 360 140 C400 80 440 30 480 0 L480 420 Z" fill="url(#artDark)"/>
    </svg>
    <div class="weight-badge">40g</div>
  </section>

  <section class="box-front box-front--milk">
    <div class="hang-tab"></div>
    <div class="brand-label"><span class="brand-mark"></span><span class="brand-name">Outback Treats</span></div>
    <p class="range-line">CHOCOLATE BOOMERANGS</p>
    <h2 class="flavour">Milk<br>Chocolate<br>Boomerang</h2>
    <svg class="artwork" viewBox="0 0 480 420" role="img" aria-label="Aboriginal dot-painting artwork of kangaroos in red, orange, cream and white">
      <defs>
        <linearGradient id="artMilk" x1="0" y1="1" x2="1" y2="0">
          <stop offset="0" stop-color="#3a1214"/>
          <stop offset=".4" stop-color="#ef8a2a"/>
          <stop offset="1" stop-color="#e4505a"/>
        </linearGradient>
      </defs>
      <path d="M0 420 L0 360 C60 320 140 300 220 280 C280 260 320 200 360 140 C400 80 440 30 480 0 L480 420 Z" fill="url(#artMilk)"/>
    </svg>
    <div class="weight-badge">40g</div>
  </section>

</main>
</body>
</html>
```